verdant terraces simple classy business card design

my name is owen harlow and I run a gardening business aimed at high class verdant terraces. the business name is verdant terraces and our logo was designed on pixel forum .My clientel are anything from residential homes to businesses. I take pride in my work and know that I offer a service like no other in my area.
The business card will be used to represent my business and I want it to be not only rememberable, but simplistic and modern. Eye catching too. Of course I would like it relatable to gardening and appealing to the correct clientel - those being garden enthusiasts, prestigious homes and businesses that are after top of the line gardening services like no other on the market.
I am not a typical lawn mowing business so I don't want a typical card design that represents that. The gardens I work with are generally million dollar properties with owners who are very garden proud looking for upkeep and guidance from me along with sometimes whole new garden designs. I want the business cards to show to my clients that I take pride, as they do, in their garden. And I want them to know from my card that I am a professional, qualified horticulturist offering them a top of the line service for life. I want them to refer my business on. I want them to look at my business card and see class and professionalism in a modern unique bold way.
The card should be simple with the possibility of the logo on the front being embossed/debossed and my details on the back the card should have a organic garden feel it's very important to me that it is absolutely perfect
I am also very open to ideas and suggestions so look forward to seeing the designs. the business logo has been supplied with this project and I want the card to be double sided

Contact info is
Owen Harlow - Managing Director / Horticulturist
Phone : 0481 526 704
Email: owenharlow@verdantterraces.com.au

Target Market(s)

high class gardens residential and commercial

Industry/Entity Type

Gardener

Contact Information for Business Card

Contact info is
Phone : 0481 526 704

PLEASE MAKE CARD DOUBLE SIDED

Requirements
Must have
• organic simple classy modern feel
• must flow with the current logo that has been supplied with this project
• Double sided
• Must explain in a simple way that I deal with high end gardens and I'm a qualified horticulturist
Nice to have
• embossed debossed logo
Should not have
• shouldn't be to busy or cheap looking

```html
<!DOCTYPE html>
<html lang="en">
<head>
<meta charset="utf-8">
<title>Verdant Terraces — Business Card</title>
<link href="https://fonts.googleapis.com/css2?family=Open+Sans:wght@400;600&display=swap" rel="stylesheet">
<style>
  :root {
    --bg: #e9ebe7;
    --card: #ffffff;
    --card-shade: #f1f2f1;
    --green: #6ab35c;
    --green-deep: #4f9a45;
    --green-soft: #8fc784;
    --ink: #5aa84d;
  }
  * { margin: 0; padding: 0; box-sizing: border-box; }
  html, body {
    width: 1200px; height: 1023px; overflow: hidden;
    background: var(--bg);
    font-family: "Open Sans", Arial, sans-serif;
  }
  .canvas { position: relative; width: 1200px; height: 1023px; }
  .card {
    position: absolute; width: 560px; height: 320px;
    background: linear-gradient(135deg, var(--card) 0%, var(--card-shade) 100%);
    box-shadow: 0 10px 28px rgba(0,0,0,.18);
    overflow: hidden;
  }
  .card--front { left: 40px; top: 120px; }
  .card--back { left: 600px; top: 583px; }

  .front-swoosh { position: absolute; inset: 0; }

  .wordmark {
    position: absolute; color: var(--ink); font-weight: 400;
    text-transform: uppercase; display: flex; align-items: center; gap: 14px;
  }
  .wordmark__dot {
    width: 54px; height: 54px; border-radius: 50%; background: var(--green-soft);
  }
  .wordmark__name { line-height: 1.15; }
  .wordmark__name span { display: block; }
  .card--front .wordmark { left: 60px; top: 120px; font-size: 30px; letter-spacing: 3px; }
  .card--front .wordmark__name span:last-child { font-size: 17px; letter-spacing: 14px; }

  .card--back .wordmark { left: 30px; top: 28px; font-size: 22px; letter-spacing: 2px; gap: 10px; }
  .card--back .wordmark__dot { width: 40px; height: 40px; }
  .card--back .wordmark__name span:last-child { font-size: 13px; letter-spacing: 10px; }

  .back-band {
    position: absolute; left: 0; right: 0; bottom: 0; height: 26px;
    background: linear-gradient(90deg, var(--green-deep) 0%, var(--green) 60%, #cfe2cb 100%);
  }
  .person { position: absolute; left: 300px; top: 128px; color: var(--ink); }
  .person__name {
    font-size: 20px; font-weight: 600; display: flex; align-items: center; gap: 8px;
  }
  .person__title { font-size: 16px; margin-top: 2px; }

  .contact { position: absolute; left: 30px; bottom: 44px; color: var(--ink); font-size: 17px; }
  .contact__row { display: flex; align-items: center; gap: 9px; line-height: 1.55; }
  .contact__row svg { flex: none; }
</style>
</head>
<body>
<main class="canvas">

  <section class="card card--front" aria-label="Card front">
    <svg class="front-swoosh" viewBox="0 0 560 320" preserveAspectRatio="none" aria-hidden="true">
      <path d="M395 0 C470 40 470 170 440 320 L470 320 C505 170 500 50 430 0 Z" fill="var(--green)"/>
      <path d="M475 0 C540 40 545 170 515 320 L560 320 L560 0 Z" fill="var(--green)"/>
      <path d="M455 0 C520 40 525 170 495 320 L515 320 C545 170 540 40 475 0 Z" fill="#eef0ee"/>
    </svg>
    <div class="wordmark">
      <div class="wordmark__dot"></div>
      <div class="wordmark__name"><span>Verdant</span><span>Terraces</span></div>
    </div>
  </section>

  <section class="card card--back" aria-label="Card back">
    <div class="wordmark">
      <div class="wordmark__dot"></div>
      <div class="wordmark__name"><span>Verdant</span><span>Terraces</span></div>
    </div>

    <div class="person">
      <div class="person__name">
        <svg width="24" height="16" viewBox="0 0 24 16" aria-hidden="true">
          <path d="M1 15 C4 3 14 0 23 1 C21 11 12 16 1 15 Z" fill="var(--green-soft)"/>
        </svg>
        Owen Harlow
      </div>
      <div class="person__title">Managing Director / Horticulturist</div>
    </div>

    <div class="contact">
      <div class="contact__row">
        <svg width="14" height="14" viewBox="0 0 14 14" aria-hidden="true">
          <path d="M3 1 L5.5 1 L6.5 4 L5 5 C5.8 7 7 8.2 9 9 L10 7.5 L13 8.5 L13 11 C13 12 12 13 11 13 C6 12.5 1.5 8 1 3 C1 2 2 1 3 1 Z" fill="var(--ink)"/>
        </svg>
        0481 526 704
      </div>
      <div class="contact__row">
        <svg width="14" height="14" viewBox="0 0 14 14" aria-hidden="true">
          <circle cx="7" cy="7" r="6" fill="none" stroke="var(--ink)" stroke-width="1.4"/>
          <path d="M1 7 H13 M7 1 C4 4 4 10 7 13 M7 1 C10 4 10 10 7 13" fill="none" stroke="var(--ink)" stroke-width="1"/>
        </svg>
        owenharlow@verdantterraces.com.au
      </div>
    </div>

    <div class="back-band"></div>
  </section>

</main>
</body>
</html>
```